Moder Business Card Design for Renewables Business

Need a business card design for my business. We collect & repurpose spent coffee ground from cafes. The cards will be made from recycled paper. Needs to fit our corporate colour scheme of white, green & brown (see logo for colour codes). Eco friendly, modern, intresting & eye catching.
This card needs to convey the message of the business and fit into its mantra of eco-friendly, sustainable etc.

Target Market(s)

Cafe Owners, Coffee Drinkers, Recycling Companies, Farmers

Industry/Entity Type

Recycling

Contact Information for Business Card

Name; Peter Halloran
Phone; 0412 386 527
e-mail; info@lumatrove.com.au
website; www.lumatrove.com.au

Font styles to use
Sans Serif
Script

Colors

Designer to choose colors to be used in the design.

Requirements
Must have
• FRONT;
• Logo, Name (Peter Halloran), phone number, e-mail address, website
• BACK;
• On the back in cursive text; 'SUSTAINABILITY IN THE DAILY GRIND'
• Small facebook & Instagram logos with text 'Lumatrove'
Should not have
• messy design

```html
<!DOCTYPE html>
<html lang="en">
<head>
<meta charset="utf-8">
<title>Lumatrove – Business Card</title>
<link href="https://fonts.googleapis.com/css2?family=Oswald:wght@500&family=Roboto:wght@400;500&display=swap" rel="stylesheet">
<style>
  :root {
    --backdrop: #ece8e2;
    --kraft: #e0c28d;
    --kraft-light: #e6cb98;
    --kraft-dark: #d6b47c;
    --brown: #6b3a1e;
    --brown-deep: #5a2f17;
    --green: #7dbb4c;
  }
  * { margin: 0; padding: 0; box-sizing: border-box; }
  html, body {
    width: 1200px;
    height: 1047px;
    overflow: hidden;
    background: var(--backdrop);
  }
  .card {
    position: absolute;
    left: 100px;
    top: 253px;
    width: 1000px;
    height: 541px;
    background: radial-gradient(ellipse at 40% 40%, var(--kraft-light), var(--kraft) 55%, var(--kraft-dark));
    box-shadow: 0 6px 24px rgba(60, 40, 20, 0.18);
  }
  .brand {
    position: absolute;
    left: 150px;
    top: 158px;
    width: 200px;
    text-align: center;
  }
  .brand-circle {
    display: block;
    margin: 0 auto;
  }
  .brand-name {
    margin-top: 20px;
    font-family: "Roboto", sans-serif;
    font-weight: 500;
    font-size: 30px;
    letter-spacing: 0.5px;
    color: var(--brown);
  }
  .divider {
    position: absolute;
    left: 450px;
    top: 160px;
    width: 3px;
    height: 218px;
    background: var(--brown);
  }
  .contact-block {
    position: absolute;
    left: 521px;
    top: 164px;
  }
  .person-name {
    font-family: "Oswald", sans-serif;
    font-weight: 500;
    font-size: 50px;
    line-height: 1;
    letter-spacing: 1px;
    text-transform: uppercase;
    color: var(--brown-deep);
  }
  .person-title {
    margin-top: 6px;
    font-family: "Roboto", sans-serif;
    font-weight: 500;
    font-size: 22px;
    color: var(--brown-deep);
  }
  .contact-list {
    list-style: none;
    margin-top: 36px;
  }
  .contact-item {
    display: flex;
    align-items: center;
    height: 30.5px;
    font-family: "Roboto", sans-serif;
    font-weight: 500;
    font-size: 23px;
    letter-spacing: 0.6px;
    color: var(--brown-deep);
  }
  .contact-icon {
    width: 16px;
    height: 16px;
    margin-right: 17px;
    flex: none;
  }
</style>
</head>
<body>
  <div class="card">
    <div class="brand">
      <svg class="brand-circle" width="170" height="170" viewBox="0 0 170 170" aria-hidden="true">
        <circle cx="85" cy="85" r="79" fill="none" stroke="var(--green)" stroke-width="9"/>
      </svg>
      <div class="brand-name">LUMATROVE</div>
    </div>

    <div class="divider"></div>

    <div class="contact-block">
      <div class="person-name">Peter Halloran</div>
      <div class="person-title">Director</div>
      <ul class="contact-list">
        <li class="contact-item">
          <svg class="contact-icon" viewBox="0 0 16 16" aria-hidden="true">
            <path d="M3.5 1.5l2.5 3-1.5 1.6c.8 1.9 2.4 3.6 4.4 4.4L10.5 9l3 2.5-1.5 2.8C6.5 14 2 9.5 1.5 3.8z" fill="var(--brown-deep)"/>
          </svg>
          0412 386 527
        </li>
        <li class="contact-item">
          <svg class="contact-icon" viewBox="0 0 16 16" aria-hidden="true">
            <rect x="1.5" y="3.5" width="13" height="9" fill="none" stroke="var(--brown-deep)" stroke-width="1.6"/>
            <path d="M1.5 3.5l6.5 5 6.5-5" fill="none" stroke="var(--brown-deep)" stroke-width="1.6"/>
          </svg>
          info@lumatrove.com.au
        </li>
        <li class="contact-item">
          <svg class="contact-icon" viewBox="0 0 16 16" aria-hidden="true">
            <g fill="none" stroke="var(--brown-deep)" stroke-width="1.4">
              <circle cx="8" cy="8" r="6.5"/>
              <ellipse cx="8" cy="8" rx="3" ry="6.5"/>
              <path d="M1.5 8h13M2.5 5h11M2.5 11h11"/>
            </g>
          </svg>
          www.lumatrove.com.au
        </li>
      </ul>
    </div>
  </div>
</body>
</html>
```